Two Wine Labels, One Red One White

We are looking to create a brand image for our wines. There are two requirements by law that we need, however beyond that, the creativity comes from the designer. Required are:
On The Red Label, Alcohol 14.1White Label Alcohol 12.5, The Size, 750ML
SO One label for the red wine with alcohol at 14.1 in a 750 ML Bottle, and one Label for white with alcohol at 12.5 in a 750 ML bottle.

Hi All:
I have some more clarity to assist in the design work.
The Brand Name of the wine is Velmaric for both the red and the white
The name should appear as Velmaric with the Brackets around phonetical as seen here
[vel-mah-reek] Both the word and the phonetical spelling should appear.
and can be seen on wordlorebin.example The Brand Name text can be black
Label should be very light grey, I am trying to capture a Stone grey or texture from stone, although, NOT Marble.
The Red Label, The word "Red" should be in red
The White Label, The word "White" should be in White, all the original remaining elements remain as originally posted.

I look forward to hearing from you for any additional questions.
Updates

Just added a logo Not really seeing what we are trying to achieve, maybe using the logo in the design may assist

Target Market(s)

Wine Aficionados

Requirements
Must have
• Details described in Project Description above, these are required by law. The Name of the Brand will be posted shortly. For the moment if you take the project, just place red on one label and white on the other.
Nice to have
• These two wines are from California (USA), so the Sierra Nevada Mountains could be an inspiration, to outline of California or coast line, a vineyard (of course), a vine...We are in silicon valley, so there is a map of silicon valley with the Bay and ocean, something from a map could work, or let your creativity flow and not use any of these concepts.
Should not have
• I do not not care for decorative fonts, however all else is open

```html
<!DOCTYPE html>
<html lang="en">
<head>
<meta charset="utf-8">
<title>Velmaric Wine Labels</title>
<link rel="stylesheet" href="https://fonts.googleapis.com/css2?family=Cinzel:wght@400;700&family=Gentium+Book+Plus&display=swap">
<style>
  :root {
    --backdrop: #1d1c18;
    --label-stone: #f1efe8;
    --label-edge: #d9d5ca;
    --ink: #1b1a18;
    --wine-red: #d8262a;
    --white-fill: #ffffff;
    --frame: #8a857b;
    --scene-olive: #8d8a6c;
    --scene-sepia: #5b5548;
  }
  * { box-sizing: border-box; margin: 0; padding: 0; }
  html, body { width: 1177px; height: 1200px; overflow: hidden; }
  body {
    background: var(--backdrop);
    position: relative;
    font-family: "Gentium Book Plus", Georgia, serif;
    color: var(--ink);
  }
  .label {
    position: absolute;
    background: linear-gradient(160deg, #f5f3ee 0%, var(--label-stone) 55%, #e9e6de 100%);
    box-shadow: inset 0 0 0 1px var(--label-edge);
    text-align: center;
  }
  .front-label { width: 320px; height: 534px; left: 315px; }
  .back-label { width: 192px; height: 288px; left: 670px; }
  .row-red .front-label { top: 30px; }
  .row-red .back-label { top: 166px; }
  .row-white .front-label { top: 618px; }
  .row-white .back-label { top: 754px; }

  .vineyard-scene {
    position: absolute;
    left: 29px; top: 10px;
    width: 262px; height: 196px;
    background: linear-gradient(180deg, #b3ad9d 0%, var(--scene-sepia) 55%, #8f8877 100%);
    border: 3px solid var(--frame);
  }
  .row-red .vineyard-scene { background: linear-gradient(180deg, #b3ad9d 0%, var(--scene-sepia) 55%, #9a8f86 100%); }
  .row-white .vineyard-scene { background: linear-gradient(180deg, #b6b29c 0%, var(--scene-sepia) 55%, var(--scene-olive) 100%); }

  .brand-name {
    font-family: "Cinzel", Georgia, serif;
    font-weight: 400;
    letter-spacing: 1px;
  }
  .phonetic { font-family: "Gentium Book Plus", Georgia, serif; }
  .front-label .brand-name { position: absolute; top: 250px; width: 100%; font-size: 37px; line-height: 1; }
  .front-label .phonetic { position: absolute; top: 294px; width: 100%; font-size: 20px; }

  .variety {
    font-family: "Cinzel", Georgia, serif;
    font-weight: 700;
    line-height: 1;
  }
  .variety-red { color: var(--wine-red); }
  .variety-white { color: var(--white-fill); -webkit-text-stroke: 1.2px var(--ink); font-weight: 400; }
  .front-label .variety { position: absolute; top: 356px; width: 100%; font-size: 62px; }
  .front-label .variety-white { font-size: 60px; letter-spacing: 1px; }
  .wine-word { font-family: "Cinzel", Georgia, serif; }
  .front-label .wine-word { position: absolute; top: 418px; width: 100%; font-size: 30px; line-height: 1; }

  .legal-line {
    position: absolute; left: 26px; right: 26px; top: 490px;
    display: flex; justify-content: space-between;
    font-size: 17px;
  }

  .back-frame {
    position: absolute; inset: 7px;
    border: 1.5px solid var(--frame);
  }
  .back-label .brand-name { position: absolute; top: 24px; width: 100%; font-size: 22px; line-height: 1; }
  .back-label .phonetic { position: absolute; top: 48px; width: 100%; font-size: 13px; }
  .back-label .variety { position: absolute; top: 74px; width: 100%; font-size: 34px; }
  .back-label .variety-white { font-size: 28px; top: 78px; }
  .back-label .wine-word { position: absolute; top: 110px; width: 100%; font-size: 21px; line-height: 1; }
  .side-note {
    position: absolute; top: 110px;
    font-size: 15px; white-space: nowrap;
  }
  .side-volume { left: 26px; transform: translate(-50%, -50%) rotate(-90deg); }
  .side-strength { right: 26px; transform: translate(50%, -50%) rotate(90deg); }
  .barcode-box {
    position: absolute; left: 24px; top: 172px;
    width: 144px; height: 62px;
    border: 1.5px solid var(--ink);
    display: flex; align-items: center; justify-content: center;
    font-size: 17px;
  }
</style>
</head>
<body>
  <section class="label-set row-red">
    <article class="label front-label">
      <div class="vineyard-scene" role="img" aria-label="Sepia terraced vineyard hillside with a barn, framed by posts hung with red grape clusters"></div>
      <h1 class="brand-name">VELMARIC</h1>
      <p class="phonetic">[vel-mah-reek]</p>
      <p class="variety variety-red">RED</p>
      <p class="wine-word">WINE</p>
      <div class="legal-line"><span>Net 750ml</span><span>14.1% alc./vol.</span></div>
    </article>
    <article class="label back-label">
      <div class="back-frame"></div>
      <h2 class="brand-name">VELMARIC</h2>
      <p class="phonetic">[vel-mah-reek]</p>
      <span class="side-note side-volume">750ml</span>
      <p class="variety variety-red">RED</p>
      <p class="wine-word">WINE</p>
      <span class="side-note side-strength">14.1% alc.</span>
      <div class="barcode-box">BARCODE</div>
    </article>
  </section>

  <section class="label-set row-white">
    <article class="label front-label">
      <div class="vineyard-scene" role="img" aria-label="Sepia terraced vineyard hillside with a barn, framed by posts hung with green grape clusters"></div>
      <h1 class="brand-name">VELMARIC</h1>
      <p class="phonetic">[vel-mah-reek]</p>
      <p class="variety variety-white">WHITE</p>
      <p class="wine-word">WINE</p>
      <div class="legal-line"><span>Net 750ml</span><span>12.5% alc./vol.</span></div>
    </article>
    <article class="label back-label">
      <div class="back-frame"></div>
      <h2 class="brand-name">VELMARIC</h2>
      <p class="phonetic">[vel-mah-reek]</p>
      <span class="side-note side-volume">750ml</span>
      <p class="variety variety-white">WHITE</p>
      <p class="wine-word">WINE</p>
      <span class="side-note side-strength">12.5% alc.</span>
      <div class="barcode-box">BARCODE</div>
    </article>
  </section>
</body>
</html>
```